Homemaking training schools needs a Business Card design

Designer, Hello!

No special requirements, good-looking enough.
--------------------------------------------------------------------------

Name: Marcus Liao
Chairman
Tel: 0574-57418263
Mobile: 13852247106
Email: kelvory@mailpond.com
Web: www.tqb2031.com
Add: No.258, LinfengJie, DaoyueQu, Ningbo, Zhejiang

LOGO
Ningbo TQB Homemaking Training School

Target Market(s)

pregnant women, mothers, infants, the elderly and families, including cleaning, cooking, nursing training.

Industry/Entity Type

Business

Contact Information for Business Card

Name: Marcus Liao
Chairman
Tel: 0574-57418263
Mobile: 13852247106
Email: kelvory@mailpond.com
Web: www.tqb2031.com

LOGO

Font styles to use
Serif
Sans Serif
Decorative

Requirements
Nice to have
• Feels: clean, specifications, safety, comfort, warmth and happiness.

```html
<!DOCTYPE html>
<html lang="en">
<head>
<meta charset="utf-8">
<title>Tian QiBao Business Card</title>
<link href="https://fonts.googleapis.com/css2?family=Montserrat:ital,wght@0,700;1,500&family=Oswald:wght@600&family=Quicksand:wght@500&display=swap" rel="stylesheet">
<style>
  :root {
    --bg: #e9e9ea;
    --card: #ffffff;
    --blue: #6a90c4;
    --blue-deep: #3f73b5;
    --pink: #e0509a;
    --ink: #2e2e30;
    --rule: #5a5a5e;
  }
  * { box-sizing: border-box; margin: 0; padding: 0; }
  html, body { width: 1200px; height: 720px; overflow: hidden; }
  body {
    background: var(--bg);
    font-family: "Quicksand", sans-serif;
    color: var(--ink);
    position: relative;
  }
  .card {
    position: absolute;
    top: 190px;
    width: 540px;
    height: 320px;
    background: var(--card);
    box-shadow: 0 6px 18px rgba(0,0,0,0.08);
  }
  .card--front { left: 40px; }
  .card--back { left: 620px; }

  /* Front */
  .brand {
    position: absolute;
    left: 0; right: 0; top: 96px;
    text-align: center;
    font-family: "Quicksand", sans-serif;
    font-weight: 500;
    font-size: 40px;
    line-height: 1;
    color: var(--ink);
  }
  .brand-rule {
    position: absolute;
    left: 120px; right: 120px; top: 162px;
    border-top: 1px solid var(--rule);
  }
  .school {
    position: absolute;
    left: 0; right: 0; top: 226px;
    text-align: center;
    font-size: 19px;
    font-weight: 500;
    color: var(--ink);
  }

  /* Back */
  .accent {
    position: absolute;
    left: 50%;
    width: 80px;
    height: 3px;
    margin-left: -40px;
    background: linear-gradient(90deg, var(--blue-deep) 50%, var(--pink) 50%);
  }
  .accent--top { top: 28px; }
  .accent--bottom { bottom: 22px; background: linear-gradient(90deg, var(--pink) 50%, var(--blue-deep) 50%); }
  .person {
    position: absolute;
    left: 0; right: 0; top: 42px;
    text-align: center;
  }
  .person__name {
    font-family: "Oswald", sans-serif;
    font-weight: 600;
    font-size: 30px;
    color: var(--blue);
    letter-spacing: 0.5px;
    text-transform: uppercase;
    line-height: 1.1;
  }
  .person__role {
    font-family: "Montserrat", sans-serif;
    font-size: 10px;
    font-style: italic;
    font-weight: 500;
    color: var(--blue);
    letter-spacing: 1px;
    text-transform: uppercase;
  }
  .address {
    position: absolute;
    left: 0; right: 0; top: 122px;
    text-align: center;
    font-family: "Montserrat", sans-serif;
    font-weight: 700;
    font-size: 15px;
    line-height: 1.5;
    color: var(--ink);
  }
  .contacts {
    position: absolute;
    left: 60px; right: 50px; top: 188px;
    list-style: none;
  }
  .contact {
    display: flex;
    align-items: center;
    height: 30px;
  }
  .contact__icon {
    width: 22px; height: 22px;
    background: var(--blue-deep);
    display: flex;
    align-items: center;
    justify-content: center;
    flex: none;
  }
  .contact__link {
    width: 12px;
    border-top: 1px solid var(--rule);
    flex: none;
  }
  .contact__text {
    margin-left: 6px;
    font-size: 17px;
    font-weight: 500;
    color: var(--blue-deep);
    white-space: nowrap;
  }
  .contact__leader {
    flex: 1;
    margin-left: 10px;
    border-top: 1px solid var(--rule);
    position: relative;
  }
  .contact__leader::after {
    content: "";
    position: absolute;
    right: 0; top: -6px;
    height: 11px;
    border-right: 1px solid var(--rule);
  }
</style>
</head>
<body>
  <section class="card card--front">
    <p class="brand">Tian QiBao</p>
    <span class="brand-rule"></span>
    <p class="school">Ningbo TQB Homemaking Training School</p>
  </section>

  <section class="card card--back">
    <span class="accent accent--top"></span>
    <div class="person">
      <h1 class="person__name">Marcus Liao</h1>
      <p class="person__role">Chairman</p>
    </div>
    <p class="address">No. 258, LinfengJie, DaoyueQu<br>Ningbo, Zhejiang</p>
    <ul class="contacts">
      <li class="contact">
        <span class="contact__icon">
          <svg width="12" height="14" viewBox="0 0 12 14" aria-hidden="true"><rect x="2" y="0.5" width="8" height="13" rx="1.5" fill="none" stroke="#fff" stroke-width="1.3"/><circle cx="6" cy="11" r="0.9" fill="#fff"/></svg>
        </span>
        <span class="contact__link"></span>
        <span class="contact__text">0574 57418263 | 138 5224 7106</span>
        <span class="contact__leader"></span>
      </li>
      <li class="contact">
        <span class="contact__icon">
          <svg width="14" height="10" viewBox="0 0 14 10" aria-hidden="true"><rect x="0.6" y="0.6" width="12.8" height="8.8" fill="none" stroke="#fff" stroke-width="1.2"/><path d="M0.8 0.8 L7 5.6 L13.2 0.8" fill="none" stroke="#fff" stroke-width="1.2"/></svg>
        </span>
        <span class="contact__link"></span>
        <span class="contact__text">kelvory@mailpond.com</span>
        <span class="contact__leader"></span>
      </li>
      <li class="contact">
        <span class="contact__icon">
          <svg width="14" height="14" viewBox="0 0 14 14" aria-hidden="true"><circle cx="7" cy="7" r="6" fill="none" stroke="#fff" stroke-width="1.2"/><ellipse cx="7" cy="7" rx="2.6" ry="6" fill="none" stroke="#fff" stroke-width="1"/><path d="M1 7 H13" stroke="#fff" stroke-width="1"/></svg>
        </span>
        <span class="contact__link"></span>
        <span class="contact__text">www.tqb2031.com</span>
        <span class="contact__leader"></span>
      </li>
    </ul>
    <span class="accent accent--bottom"></span>
  </section>
</body>
</html>
```